Fishing charter business in Sitka Alaska needs new business card design

I have had the same design for 10 plus years, ready for something different. I have attached a copy of my current card and my website link is www.bluecoveangling.net
I am looking for something that will catch my clients eye, although I rely on word of mouth for most of my business a a nice business card will help people remember who I am. My business is located in Sitka Alaska, there are probably 20-30 other charter businesses in Sitka. I like the way my current card is laid out, with the two tone black and grey. I can leave it up to the designers to come up with something else.
Target Market(s)
men, women, couples. Anyone who likes fishing
Industry/Entity Type
Tourism
Contact Information for Business Card
Dorrance's Charter Service
Tidewater Rockline Sportfishing
Colors
Designer to choose colors to be used in the design.
Requirements
Must have
- Gilbert Dorrance
- PO Box 4716
- Sitka, AK 99835
- Compass Rose image
- 100 Ton USCG Licensed Captain
- gdorrance@wavelink.net
- 907-555-0142
- www.bluecoveangling.net
Nice to have
- ghost image of "boat helm"
Should not have
- be to complex

```html
<!DOCTYPE html>
<html lang="en">
<head>
<meta charset="utf-8">
<title>Dorrance's Sportfishing Charters – Business Card</title>
<link href="https://fonts.googleapis.com/css2?family=Work+Sans:wght@400;500;600&display=swap" rel="stylesheet">
<style>
  :root {
    --backdrop: #9a9a9a;
    --card-white: #ffffff;
    --ink: #1e1e1e;
    --accent-blue: #1a8fd6;
    --ghost: #eef1f4;
    --sky: #c9dcee;
    --snow: #f1f5fa;
    --mountain: #7f98b4;
    --water: #3b6aa3;
    --deep-water: #2c5588;
  }
  html, body {
    margin: 0;
    width: 1200px;
    height: 930px;
    overflow: hidden;
    background: var(--backdrop);
    font-family: "Work Sans", sans-serif;
  }
  .canvas { position: relative; width: 1200px; height: 930px; }
  .card {
    position: absolute;
    width: 640px;
    height: 366px;
    border-radius: 22px;
    overflow: hidden;
    box-shadow: 0 6px 16px rgba(0,0,0,.28);
  }
  .card--front { left: 70px; top: 50px; }
  .card--back { left: 490px; top: 510px; background: var(--card-white); }

  .front-photo {
    position: absolute; inset: 0;
    background: linear-gradient(170deg,
      var(--sky) 0%,
      var(--snow) 22%,
      #dfe7f0 34%,
      var(--mountain) 50%,
      var(--water) 66%,
      var(--deep-water) 100%);
  }
  .brand-name {
    position: absolute; right: 40px; top: 40px;
    margin: 0;
    font-weight: 600; font-size: 22px; line-height: 1.2;
    color: var(--ink); text-transform: uppercase; letter-spacing: 1.5px;
    text-align: right;
  }

  .ghost-name {
    position: absolute; left: 0; right: 0; top: 44px;
    text-align: center;
    font-weight: 600; font-size: 22px;
    color: var(--ghost); text-transform: uppercase; letter-spacing: 3px;
  }
  .identity {
    position: absolute; left: 56px; top: 152px;
  }
  .identity__name {
    margin: 0; font-weight: 500; font-size: 32px; line-height: 1.1;
    color: var(--accent-blue); white-space: nowrap;
  }
  .identity__title {
    margin: 6px 0 0; font-size: 16px; color: var(--ink); white-space: nowrap;
  }
  .divider {
    position: absolute; left: 372px; top: 120px;
    width: 2px; height: 96px; background: var(--accent-blue);
  }
  .contact {
    position: absolute; left: 392px; top: 120px;
    margin: 0; padding: 0; list-style: none;
    font-size: 15px; color: var(--ink);
  }
  .contact li { display: flex; align-items: center; gap: 8px; height: 32px; white-space: nowrap; }
  .contact svg { width: 13px; height: 13px; fill: none; stroke: var(--accent-blue); stroke-width: 2; flex: none; }
  .address {
    position: absolute; left: 0; right: 0; bottom: 48px; margin: 0;
    text-align: center; font-size: 16px; color: var(--ink);
  }
</style>
</head>
<body>
<main class="canvas">
  <section class="card card--front">
    <div class="front-photo" role="img" aria-label="Photo of a captain holding a large salmon on the water, with a snow-capped volcano behind"></div>
    <p class="brand-name">Dorrance's<br>Sportfishing<br>Charters</p>
  </section>

  <section class="card card--back">
    <div class="ghost-name" aria-hidden="true">Dorrance's Sportfishing Charters</div>
    <div class="identity">
      <h1 class="identity__name">Gilbert Dorrance</h1>
      <p class="identity__title">100 Ton USCG Licensed Captain</p>
    </div>
    <div class="divider"></div>
    <ul class="contact">
      <li><svg viewBox="0 0 16 16"><path d="M3 2l3 0 1 4-2 1a9 9 0 0 0 4 4l1-2 4 1 0 3c-7 1-12-4-11-11z"/></svg>907-555-0142</li>
      <li><svg viewBox="0 0 16 16"><rect x="1.5" y="3.5" width="13" height="9"/><path d="M1.5 3.5l6.5 5 6.5-5"/></svg>gdorrance@wavelink.net</li>
      <li><svg viewBox="0 0 16 16"><circle cx="8" cy="8" r="6.5"/><path d="M1.5 8h13M8 1.5c3 3 3 10 0 13M8 1.5c-3 3-3 10 0 13"/></svg>www.bluecoveangling.net</li>
    </ul>
    <p class="address">PO Box 4716 Sitka, AK 99835</p>
  </section>
</main>
</body>
</html>
```